New Law Firm needs a business card design

I need a business card for my new law firm called Tansey Wills and Probate. I would like designs to use my logo attached. My firm is new and modern. I like the colors orange, white, grey and black. The design I will chose will be one which uses color well, one which looks impressive, smart and modern.

Target Market(s)

Adults aged 30 to 50 seeking professional advice.

Industry/Entity Type

Law Firm

Requirements
Must have
• My logo which is attached.

Must have a modern font, similar to my logo and draft business card.
Should not have
• Any symbols about law, such as scales etc.

```html
<!DOCTYPE html>
<html lang="en">
<head>
<meta charset="utf-8">
<title>Tansey Wills and Probate – Business Card</title>
<link rel="stylesheet" href="https://fonts.googleapis.com/css2?family=Norican&family=Yellowtail&family=Questrial&display=swap">
<style>
  :root {
    --orange: #f0891a;
    --orange-deep: #f68b0c;
    --grey: #6d6d6d;
    --ink: #222222;
    --paper: #ffffff;
    --canvas: #f1f1f1;
    --edge: #e2e2e2;
  }
  * { box-sizing: border-box; margin: 0; padding: 0; }
  html, body { width: 1200px; height: 1000px; overflow: hidden; }
  body {
    background: var(--canvas);
    font-family: "Questrial", "Helvetica Neue", Arial, sans-serif;
    color: var(--ink);
    position: relative;
  }
  .card {
    position: absolute;
    top: 330px;
    width: 540px;
    height: 320px;
    background: var(--paper);
    border: 1px solid var(--edge);
    overflow: hidden;
  }
  .card--front { left: 40px; }
  .card--back { left: 620px; }

  .firm-name {
    font-family: "Questrial", "Helvetica Neue", Arial, sans-serif;
    font-size: 12px;
    font-weight: 400;
    letter-spacing: 2px;
    text-transform: uppercase;
    color: var(--grey);
    line-height: 1.3;
  }

  .holder-name {
    font-family: "Norican", "Yellowtail", cursive;
    font-weight: 400;
    font-size: 32px;
    color: var(--orange);
    line-height: 1.1;
    white-space: nowrap;
  }
  .credentials {
    font-size: 13px;
    color: #333;
    margin-top: 4px;
  }

  /* Front */
  .front-block {
    position: absolute;
    left: 0; right: 0; top: 96px;
    display: flex;
    flex-direction: column;
    align-items: center;
    text-align: center;
  }
  .front-block .firm-name { margin-bottom: 18px; width: 140px; }

  /* Back */
  .identity {
    position: absolute;
    top: 26px; left: 0; right: 0;
    text-align: center;
  }
  .divider {
    width: 40px;
    height: 1px;
    background: var(--orange);
    margin: 20px auto 0;
  }
  .contact-list {
    position: absolute;
    left: 70px;
    top: 134px;
    border-left: 3px solid var(--orange);
    padding-left: 10px;
    display: grid;
    grid-template-columns: 76px auto;
    align-items: baseline;
  }
  .contact-list dt {
    font-size: 18px;
    color: var(--orange);
    line-height: 23px;
  }
  .contact-list dd {
    font-size: 14px;
    color: var(--ink);
    line-height: 23px;
  }
  .contact-list dd::before {
    content: ":";
    color: var(--orange);
    margin-right: 6px;
  }
  .card--back .firm-name {
    position: absolute;
    right: 22px;
    bottom: 34px;
    width: 130px;
    text-align: right;
    font-size: 11px;
  }
  .accent-band {
    position: absolute;
    left: 0; right: 0; bottom: 0;
    height: 18px;
    background: var(--orange-deep);
  }
</style>
</head>
<body>
  <section class="card card--front" aria-label="Business card front">
    <div class="front-block">
      <p class="firm-name">Tansey Wills and Probate</p>
      <h1 class="holder-name">Daniel Mercer - Lawyer</h1>
      <p class="credentials">Assoc.Deg.Law, BLJSt, LLB, Grad Dip Law.</p>
    </div>
  </section>

  <section class="card card--back" aria-label="Business card back">
    <div class="identity">
      <h2 class="holder-name">Daniel Mercer - Lawyer</h2>
      <p class="credentials">Assoc.Deg.Law, BLJSt, LLB, Grad Dip Law.</p>
      <div class="divider"></div>
    </div>
    <dl class="contact-list">
      <dt>Address</dt><dd>48 Harbour Lane, Brookfield, NY</dd>
      <dt>Phone</dt><dd>(+61) 955-210-4471</dd>
      <dt>Fax</dt><dd>(+61) 955-210-4471</dd>
      <dt>Email</dt><dd>daniel@tanseyprobate.com.au</dd>
    </dl>
    <p class="firm-name">Tansey Wills and Probate</p>
    <div class="accent-band"></div>
  </section>
</body>
</html>
```